Website redesign for a Cloud Advisory business

We are looking to revisit our existing brand and website, with a view to updating both. Looking for concepts and designs for how the website might look, flow and feel. Current website is: www.brellomint.com.au

Scope and Deliverables: Concept design for the home page and one internal page.

We do not expect you to design all the pages and all the elements of the website at this stage.

This job is not for the full website design, but just for concepts that we can start with when we go into the full website design.

We would love to see a design feature based on our name, logo, or industry, which can run through banners and other collateral (twitter banner, ads on Google, corporate documents etc).

We want the brand to properly depict what we bring/deliver to businesses when consulting to them and this should extend to the colour scheme, logo, font (perhaps updated) and copy (which will be supplied).

Our brand should suitably communicate our ability, knowledge and extensive experience within the Cloud space.

It should express and evoke credibility, knowledge and understanding of the Cloud space, independence, gravitas, reliability, efficiency, trust, expertise, approachability, service delivery but be uncomplicated, practical and use plain speaking language.

Colours that reinforce this might include: Blues, blacks, silver, white, grey and our existing orange.

Website designs that we like or have referenced include:

Varnolift: http://varnolift.com.au/ - This has good information but looks a little amateur in it’s cartoon like design and colour scheme. Also, this seems to be aimed at clients more interested in price than design and what we are going for is a little more high end.

Pendramoor: https://www.pendramoor.com.au/ - This site has merit in its’ setup but little call to action on the home page, especially before the scroll line. I like the set up of the Case Studies page however I’d look to make it more prominent by having it set up 3 across rather than the 4 they have. Something such as this: https://www.qandelby.com/case-studies

Tolvane: http://www.tolvane.com.au/#home4 - This page is a good one as far as selling services and information on the company. I quite like it.

MirefoldIT: http://www.mirefoldit.com.au/ - While I don’t think is particularly creative, it does practically depict the services we offer in a fairly clear way and might be a bit of a basic (albeit dull) template to follow.

JDP: https://store.jdp.com/us/Product-Family/JDP-Advisory-Services/JDP-Cloud-Advisory-Service/p/JDP-Services-Cloud-Advisory - This offers substantial information but is probably a little confusing although the roll-over drop down menus have merit.

ZEV: http://www.zev.net.au/en/services/ - While this in not quite what we are looking for, the colour scheme gives it more gravitas and quality.

As another reference, this website and the way they present their case studies is also something we like, although I’d like them shown 3 up, side by side…. https://www.qandelby.com/case-studies.

We have added a page layout and page purpose document.

Target Market(s)

Corporates, small - medium business, direct referrals, via search results

Industry/Entity Type

Business

Number of Pages Required

1 page

Font styles to use
Sans Serif

Colors
85abd2
0455a3
000000
f37122
5c5c5c

Requirements
Must have
• Website must be mobile device compatible.
• Concept design for the home page.
Nice to have
• We would love to see a design feature based on our name, logo, or industry, which can run through banners and other collateral (twitter banner, ads on Google, corporate documents etc).

```html
<!DOCTYPE html>
<html lang="en">
<head>
<meta charset="utf-8">
<title>Brellomint – Impartial Cloud Solutions</title>
<link href="https://fonts.googleapis.com/css2?family=Open+Sans:wght@300;400;600;700&display=swap" rel="stylesheet">
<style>
:root{
  --orange:#f37122;
  --orange-soft:#fbd9c4;
  --ink:#000000;
  --grey:#5c5c5c;
  --panel:#3b3b3b;
  --footer:#262626;
  --footer-deep:#1a1a1a;
  --white:#ffffff;
  --text-muted:#b5b5b5;
}
*{box-sizing:border-box;margin:0;padding:0}
html,body{width:804px;height:1200px;overflow:hidden}
body{font-family:"Open Sans",Arial,sans-serif;background:var(--white);position:relative;color:var(--white)}
.site-header{position:absolute;top:0;left:0;width:804px;height:43px;background:var(--white);display:flex;align-items:center;justify-content:space-between;padding:0 40px 0 40px}
.brand{display:flex;align-items:center;gap:6px;color:var(--orange);font-weight:700;font-size:19px;letter-spacing:.5px}
.brand-mark{width:14px;height:14px;background:var(--orange)}
.main-nav{display:flex;align-items:center;gap:4px;font-size:11px;color:var(--grey)}
.main-nav a{color:var(--grey);text-decoration:none;padding:4px 14px;border-radius:12px}
.main-nav a.is-active{background:var(--orange-soft);color:var(--orange)}
.hero{position:absolute;top:43px;left:0;width:804px;height:252px;background:linear-gradient(135deg,#4a4a4a,#2a2a2a 45%,#3d3a36 100%);text-align:center}
.hero-title{position:absolute;top:72px;width:100%;font-size:30px;font-weight:700}
.hero-title span{color:var(--orange)}
.hero-sub{position:absolute;top:116px;width:100%;font-size:9px;color:#ddd}
.btn{display:inline-block;background:var(--orange);color:var(--white);font-size:9px;font-weight:600;padding:7px 14px;border-radius:2px}
.hero .btn{position:absolute;top:140px;left:342px;border:1px solid #fff3}
.services{position:absolute;top:295px;left:0;width:804px;height:523px;background:#e4e4e4}
.tile{position:absolute;overflow:hidden;text-align:center}
.tile-photo{position:absolute;inset:0}
.tile-body{position:absolute;left:0;right:0;bottom:18px;padding:0 18px}
.tile h3{font-weight:600;font-size:15px;margin-bottom:4px}
.tile p{font-size:8px;color:#e6e6e6;line-height:1.35}
.t-selection{left:75px;top:18px;width:322px;height:156px}
.t-accounting{left:402px;top:18px;width:327px;height:325px}
.t-business{left:75px;top:182px;width:322px;height:327px;background:var(--orange)}
.t-business .tile-body{top:86px;bottom:auto}
.t-business h3{font-size:27px;font-weight:300;line-height:1.2;margin-bottom:10px}
.t-business p{color:#fff;font-size:9px}
.t-business .btn-light{display:inline-block;margin-top:28px;background:var(--white);color:var(--orange);font-size:9px;font-weight:600;padding:8px 18px;border-radius:3px}
.t-int-a{left:402px;top:348px;width:160px;height:161px}
.t-int-b{left:568px;top:348px;width:161px;height:161px}
.testimonial{position:absolute;top:818px;left:0;width:804px;height:107px;background:var(--panel)}
.client{position:absolute;left:110px;top:22px;width:62px;height:62px;border-radius:50%;background:#f6c21a;display:flex;align-items:center;justify-content:center;color:var(--ink);font-size:8px;font-weight:700;text-align:center;line-height:1.1}
.quote{position:absolute;left:192px;top:26px;width:480px;font-size:9px;line-height:1.5;color:#eee}
.quote cite{display:block;margin-top:8px;font-style:normal;font-weight:700;color:var(--orange);font-size:11px}
.qmark{position:absolute;font-size:54px;color:#8a8a8a;font-weight:700;line-height:1}
.qmark.open{left:180px;top:6px}
.qmark.close{left:688px;top:56px}
.site-footer{position:absolute;top:925px;left:0;width:804px;height:228px;background:var(--footer);display:flex;gap:0;padding:28px 40px 0 40px}
.f-col{width:181px;font-size:8px;color:var(--text-muted);line-height:1.5}
.f-col h4{font-size:9px;color:var(--white);font-weight:600;margin-bottom:10px}
.f-col .btn{margin-top:12px;font-size:8px}
.post{display:flex;gap:8px;margin-bottom:10px}
.post-thumb{width:34px;height:30px;background:#000;flex:none}
.store-badge{width:60px;height:20px;background:#000;border:1px solid #555;border-radius:3px;margin-bottom:8px}
.promo{width:100px;height:58px;background:var(--orange);margin-bottom:8px}
.promo-link{color:var(--orange)}
.copyright{position:absolute;top:1153px;left:0;width:804px;height:47px;background:var(--footer-deep);text-align:center;font-size:7px;color:#888;padding-top:18px}
</style>
</head>
<body>
<header class="site-header">
  <div class="brand"><span class="brand-mark"></span>Brellomint</div>
  <nav class="main-nav">
    <a class="is-active" href="#">Home</a><a href="#">Services</a><a href="#">Aboutus</a><a href="#">Blog</a><a href="#">Contact</a>
    <svg width="14" height="14" viewBox="0 0 14 14" aria-label="Search"><circle cx="6" cy="6" r="4.3" fill="none" stroke="#f37122" stroke-width="2"/><line x1="9" y1="9" x2="13" y2="13" stroke="#f37122" stroke-width="2.4"/></svg>
  </nav>
</header>

<section class="hero" role="img" aria-label="Dark photo of a desk with laptops and paperwork">
  <h1 class="hero-title"><span>Impartial</span> Cloud Solutions</h1>
  <p class="hero-sub">We provide impartial advice on cloud solutions ensuring it's always right for you.</p>
  <span class="btn">Book a Free Consultation</span>
</section>

<section class="services">
  <article class="tile t-selection">
    <div class="tile-photo" role="img" aria-label="Photo of a business team around a table" style="background:linear-gradient(160deg,#6b6f74,#2e3236)"></div>
    <div class="tile-body"><h3>System Selection</h3><p>Compare your cloud options, pick the right system and move to it with ease.</p></div>
  </article>
  <article class="tile t-accounting">
    <div class="tile-photo" role="img" aria-label="Photo of two colleagues working at a laptop" style="background:linear-gradient(150deg,#c9c4bd,#8a8178 55%,#4a4642)"></div>
    <div class="tile-body"><h3>Accounting Systems &amp; Conversions</h3><p>Convert your accounting ledgers, data and reports to a cloud platform, simple and safe.</p></div>
  </article>
  <article class="tile t-business">
    <div class="tile-body">
      <h3>Business Project &amp; Job Management</h3>
      <p>Get started with the right project and job management system for your team. We plan, set up, train and support each stage of the move.</p>
      <span class="btn-light">View More</span>
    </div>
  </article>
  <article class="tile t-int-a">
    <div class="tile-photo" role="img" aria-label="Photo of a meeting in an office" style="background:linear-gradient(160deg,#7a7570,#3a3734)"></div>
    <div class="tile-body"><h3>Integration</h3><p>Get started with the right project and integration system for you, here.</p></div>
  </article>
  <article class="tile t-int-b">
    <div class="tile-photo" role="img" aria-label="Photo of a man working at a computer" style="background:linear-gradient(160deg,#6e7379,#33373b)"></div>
    <div class="tile-body"><h3>Integration</h3><p>Get started with the right project and integration system for you, here.</p></div>
  </article>
</section>

<section class="testimonial">
  <div class="client">Fernvale<br>Studio</div>
  <span class="qmark open">“</span>
  <blockquote class="quote">I am very pleased with your service. You were particularly good to work with, very sympathetic, and quick to reply. We gained a great deal of confidence working with you and have streamlined our accounting as a result.<cite>Fernvale Studio</cite></blockquote>
  <span class="qmark close">”</span>
</section>

<footer class="site-footer">
  <div class="f-col">
    <h4>Our Office Location</h4>
    <p>Level 4, 18 Harbour Lane<br>Northwood NSW 2066<br>Phone 02 5550 1842<br>hello@brellomint.com.au</p>
    <span class="btn">Send Us A Message</span>
  </div>
  <div class="f-col">
    <h4>Top Blogs</h4>
    <div class="post"><span class="post-thumb"></span><p>Choosing a cloud ledger.<br>Five tips before you switch.<br>Read the full post</p></div>
    <div class="post"><span class="post-thumb"></span><p>Moving jobs online.<br>What small teams gain.<br>Read the full post</p></div>
  </div>
  <div class="f-col">
    <h4>Download</h4>
    <div class="store-badge"></div>
    <div class="store-badge"></div>
  </div>
  <div class="f-col">
    <h4>News &amp; Promotions</h4>
    <div class="promo"></div>
    <span class="promo-link">Read more</span>
  </div>
</footer>
<div class="copyright">Copyright © 2015 · ALL RIGHTS RESERVED BRELLOMINT</div>
</body>
</html>
```